Amber Lantern Cafe Business Card

We need a business card design for a new European Cafe. Main menu will be coffee and deserts.

Requirements
Must have
• Logo - 1 of the attached versions
Address - TBA (you can use 487 Morrow Ave Unit 9 for now)
Phone - TBA (you can use 555-238-4176 for now)

```html
<!DOCTYPE html>
<html lang="en">
<head>
<meta charset="utf-8">
<title>Amber Lantern Cafe – Business Card</title>
<link rel="stylesheet" href="https://fonts.googleapis.com/css2?family=Open+Sans:wght@300;400;600;700&display=swap">
<style>
  :root {
    --page-bg: #d9d3cc;
    --card-top: #e4e1dc;
    --ink-dark: #3a3330;
    --panel-dark: #2f2a28;
    --copper: #a2502c;
    --copper-light: #c06a3e;
    --silver: #d8d4d0;
    --text-soft: #d9b9ae;
    --text-light: #ece6e2;
  }
  * { margin: 0; padding: 0; box-sizing: border-box; }
  html, body { width: 1200px; height: 970px; overflow: hidden; }
  body { background: var(--page-bg); font-family: "Open Sans", Arial, sans-serif; position: relative; }

  .business-card {
    position: absolute; left: 172px; top: 280px;
    width: 856px; height: 466px;
    background: var(--card-top);
    overflow: hidden;
    box-shadow: 0 10px 30px rgba(0,0,0,.18);
  }
  .card-shapes { position: absolute; inset: 0; }

  .brand { position: absolute; left: 56px; top: 53px; display: flex; align-items: center; gap: 24px; }
  .brand-square { width: 120px; height: 122px; background: var(--ink-dark); border-radius: 3px; }
  .brand-name { font-size: 40px; font-weight: 400; color: var(--ink-dark); line-height: 1.15; width: 330px; }

  .contact { position: absolute; left: 53px; top: 355px; color: var(--text-soft); font-size: 18px; font-weight: 400; }
  .contact-address { margin-bottom: 14px; }
  .contact-row { display: flex; align-items: center; gap: 14px; }
  .contact-item { display: flex; align-items: center; gap: 8px; }
  .contact-icon { width: 22px; height: 22px; }

  .person { position: absolute; right: 53px; top: 355px; text-align: right; }
  .person-name { font-size: 22px; font-weight: 700; letter-spacing: 1px; color: var(--copper-light); }
  .person-title { font-size: 18px; color: var(--text-light); margin-top: 2px; }
</style>
</head>
<body>
  <div class="business-card">
    <svg class="card-shapes" width="856" height="466" viewBox="0 0 856 466">
      <path class="wave-band" fill="var(--copper)"
        d="M0,205 C220,192 380,240 560,238 C720,236 780,204 856,200 L856,240 C780,244 700,262 560,266 C380,270 220,238 0,238 Z"/>
      <path class="wave-silver" fill="var(--silver)"
        d="M0,238 C220,238 380,270 560,266 C700,262 780,244 856,240 L856,250 C780,254 700,274 560,278 C380,282 220,250 0,248 Z"/>
      <path class="dark-panel" fill="var(--panel-dark)"
        d="M0,248 C220,250 380,282 560,278 C700,274 780,254 856,250 L856,466 L0,466 Z"/>
    </svg>

    <div class="brand">
      <div class="brand-square"></div>
      <div class="brand-name">Amber Lantern Cafe</div>
    </div>

    <div class="contact">
      <p class="contact-address">487 Morrow Ave Unit 9, Fairbrook, ON K0X2B7</p>
      <div class="contact-row">
        <span class="contact-item">
          <svg class="contact-icon" viewBox="0 0 22 22" aria-hidden="true">
            <circle cx="11" cy="11" r="10" fill="none" stroke="var(--copper)" stroke-width="1.5"/>
            <path d="M7.5,6 L9.5,6 L10.3,8.5 L9,9.6 C9.7,11 10.9,12.3 12.4,13 L13.5,11.7 L16,12.5 L16,14.5 C16,15.2 15.4,15.7 14.7,15.6 C10.3,15 7,11.7 6.4,7.3 C6.3,6.6 6.8,6 7.5,6 Z" fill="var(--copper)"/>
          </svg>
          555-238-4176
        </span>
        <span class="contact-item">
          <svg class="contact-icon" viewBox="0 0 22 22" aria-hidden="true">
            <circle cx="11" cy="11" r="10" fill="none" stroke="var(--copper)" stroke-width="1.5"/>
            <rect x="5.5" y="7.5" width="11" height="7.5" fill="none" stroke="var(--copper)" stroke-width="1.4"/>
            <path d="M5.5,7.5 L11,12 L16.5,7.5" fill="none" stroke="var(--copper)" stroke-width="1.4"/>
          </svg>
          info@amberlantern.com
        </span>
      </div>
    </div>

    <div class="person">
      <p class="person-name">JORDAN PELL</p>
      <p class="person-title">Manager</p>
    </div>
  </div>
</body>
</html>
```